Jolly Paws Business Card Update

I have a business card which I love. I want to keep the same logo, colours, font and style. I want to upgrade the scripting and remove some elements and add others.
On the front side under Services - remove the existing wording and insert - Providing individual coaching strategies to create happy, healthy and social canine companions
Under Rebecca Thornley amend the current wording to read: Qualified in Dog Behavioural Training, Natural Animal Healthcare and Animal Health Science
On the reverse side to remove the web address.

```html
<!DOCTYPE html>
<html lang="en">
<head>
<meta charset="utf-8">
<title>Jolly Paws Business Card</title>
<link rel="stylesheet" href="https://fonts.googleapis.com/css2?family=Arimo:wght@400;700&display=swap">
<style>
  :root {
    --page-bg: #ececec;
    --blue-light: #0ea2dc;
    --blue-deep: #1b3f96;
    --red-bright: #e0242a;
    --red-mid: #a3161c;
    --red-deep: #6a0c10;
    --cream: #efe7cf;
    --gold: #d8c79a;
    --white: #ffffff;
  }
  * { box-sizing: border-box; margin: 0; padding: 0; }
  html, body { width: 1200px; height: 964px; overflow: hidden; }
  body {
    background: var(--page-bg);
    font-family: "Arimo", Arial, sans-serif;
    color: var(--white);
    position: relative;
  }
  .card {
    position: absolute;
    left: 210px;
    width: 780px;
    height: 420px;
    overflow: hidden;
    box-shadow: 0 6px 18px rgba(0,0,0,0.18);
  }
  .card-front { top: 42px; background: linear-gradient(180deg, var(--blue-light) 0%, var(--blue-deep) 75%); }
  .card-back { top: 502px; background: linear-gradient(180deg, var(--blue-light) 0%, #0a76bf 100%); }
  .card-shape { position: absolute; inset: 0; }

  .brand-mark {
    position: absolute;
    border-radius: 50%;
    background: var(--cream);
    border: 7px solid var(--red-mid);
  }
  .brand-name {
    position: absolute;
    font-weight: 700;
    color: var(--cream);
    white-space: nowrap;
  }

  .front-brand {
    position: absolute;
    left: 170px;
    top: 28px;
    width: 380px;
    text-align: center;
  }
  .card-front .brand-mark { position: relative; display: block; margin: 0 auto; width: 140px; height: 140px; }
  .card-front .brand-name { position: static; display: block; margin-top: 10px; font-size: 46px; letter-spacing: 2px; line-height: 54px; }
  .tagline {
    display: block;
    margin-top: 4px;
    font-size: 20px;
    letter-spacing: 1px;
    color: var(--white);
    white-space: nowrap;
  }

  .back-brand {
    position: absolute;
    left: 100px;
    top: 56px;
    width: 160px;
    text-align: center;
  }
  .card-back .brand-mark { position: relative; display: block; margin: 0 auto; width: 128px; height: 128px; }
  .card-back .brand-name { position: static; display: block; margin-top: 10px; font-size: 19px; letter-spacing: 1px; }
  .services-divider {
    position: absolute; left: 330px; top: 62px; width: 1px; height: 150px;
    background: rgba(255,255,255,0.7);
  }
  .services { position: absolute; left: 352px; top: 78px; width: 400px; }
  .services-title { font-size: 21px; margin-bottom: 6px; }
  .services-text { font-size: 19px; line-height: 1.3; }

  .mission-band {
    position: absolute; left: 0; top: 240px; width: 100%; height: 30px;
    background: var(--cream);
    color: #1d1d1d;
    font-size: 16px;
    line-height: 30px;
    text-align: center;
  }
  .contact-area {
    position: absolute; left: 0; top: 270px; width: 100%; height: 150px;
    background: radial-gradient(ellipse at 45% 55%, var(--red-bright) 0%, var(--red-mid) 45%, var(--red-deep) 100%);
  }
  .person { position: absolute; left: 90px; top: 18px; width: 400px; text-align: center; }
  .person-name { font-size: 25px; margin-bottom: 6px; }
  .person-quals { font-size: 17px; line-height: 1.3; }
  .contact-divider {
    position: absolute; left: 510px; top: 22px; width: 1px; height: 100px;
    background: rgba(255,255,255,0.75);
  }
  .contacts { position: absolute; left: 528px; top: 38px; font-size: 16px; }
  .contact-line { display: flex; align-items: center; gap: 9px; height: 30px; white-space: nowrap; }
  .contact-icon { width: 18px; height: 18px; flex: none; }
</style>
</head>
<body>

  <section class="card card-front" aria-label="Card front">
    <svg class="card-shape" viewBox="0 0 780 420" width="780" height="420" aria-hidden="true">
      <defs>
        <radialGradient id="frontRed" cx="0.45" cy="0.75" r="0.7">
          <stop offset="0" stop-color="#e0242a"/>
          <stop offset="0.5" stop-color="#a3161c"/>
          <stop offset="1" stop-color="#6a0c10"/>
        </radialGradient>
      </defs>
      <path d="M0 380 Q 400 345 780 250 L780 420 L0 420 Z" fill="url(#frontRed)"/>
      <path d="M0 380 Q 400 345 780 250" fill="none" stroke="#d8c79a" stroke-width="4"/>
    </svg>
    <div class="front-brand">
      <div class="brand-mark"></div>
      <div class="brand-name">JOLLY PAWS</div>
      <div class="tagline">HAPPY DOGS, HAPPY OWNERS</div>
    </div>
  </section>

  <section class="card card-back" aria-label="Card back">
    <div class="back-brand">
      <div class="brand-mark"></div>
      <div class="brand-name">Jolly Paws</div>
    </div>
    <div class="services-divider"></div>
    <div class="services">
      <div class="services-title">SERVICES</div>
      <div class="services-text">Providing individual coaching strategies to create happy, healthy and social canine companions</div>
    </div>

    <div class="mission-band">Promoting communication and connection between dogs and their families</div>

    <div class="contact-area">
      <div class="person">
        <div class="person-name">Rebecca Thornley</div>
        <div class="person-quals">Qualified in Dog Behavioural Training,<br>Natural Animal Healthcare and<br>Animal Health Science</div>
      </div>
      <div class="contact-divider"></div>
      <div class="contacts">
        <div class="contact-line">
          <svg class="contact-icon" viewBox="0 0 18 18" aria-hidden="true">
            <circle cx="9" cy="9" r="9" fill="#ffffff"/>
            <rect x="6" y="3.5" width="6" height="11" rx="1.2" fill="#a3161c"/>
            <rect x="7" y="5" width="4" height="6" fill="#ffffff"/>
          </svg>
          <span>0412 708 356</span>
        </div>
        <div class="contact-line">
          <svg class="contact-icon" viewBox="0 0 18 18" aria-hidden="true">
            <circle cx="9" cy="9" r="9" fill="#ffffff"/>
            <rect x="4" y="5.5" width="10" height="7" fill="#a3161c"/>
            <path d="M4 5.5 L9 9.5 L14 5.5" fill="none" stroke="#ffffff" stroke-width="1"/>
          </svg>
          <span>hello@jollypawscoach.com</span>
        </div>
      </div>
    </div>
  </section>

</body>
</html>
```